I’d like to see something with similar colors and design concept to the “Your Wallet Knows the Way” book included in attchment

Create a book cover with front cover, and full front, spine and back cover spread.
Simple and clean design. See design inspiration below.
Size 6X9
Title of the book: Find Your Shelf! Veteran Editors Reveal Quiet Methods

Please leave space for 6 authors names on the front cover. Authors names will be provided at a later time.

Back of book should included the name of the publishing company:
Lantern Grove Publishing

As well as the following synopsis
The landscape of the publishing industry is changing. Gone are the days of coveted gatekeepers controlling content and dictating the messages being distributed. With the rise of technology, social media , self-publishing platforms, and independent bookstores, there are increased opportunities for people to share their ideas, messages, and stories with the world through books. The types of books that we’re publishing are also evolving — mini-books, audio books, journals, multi-author books, cook books, children’s books, comic books, coloring books, interactive books, tarot and oracle card decks are all expanding the podium for people to express ideas and influence the culture. More and more entrepreneurs are posturing themselves as thought leaders by leveraging this growing platform.
But that doesn't mean it’s easy.
Even with the expanding platforms and opportunities, only a fraction of people with publishing ambitions are able to achieve this coveted dream held by so many. It can be a daunting process for budding authors trying to maneuver through the writing, packaging, marketing, and publishing processes alone.

In this book you'll find passionate, purpose-driven, and well-versed experts working in the various areas of publishing, eager to help open your eyes to the promise of publishing and effortlessly guide you through the process.

Colors
0094D4
00A9DD
6FCCEA
C7EBF8
E9F6FB
FFF300
FFF600
FEFA6F
FFFEC7
FFFEE8
FFC000
F8CF3A
FAE287
FDF2CF
FEFAEE
F0912C
F2A743
F7CA91
FBE8D2
FDF5EE
EE7325
F08F49
F5BC92
FAE3D3
FDF4ED
6B429C
8869AF
B7A5CE
E3DAEB
F3F0F8

```html
<!DOCTYPE html>
<html lang="en">
<head>
<meta charset="utf-8">
<title>Find Your Shelf! — Cover Spread</title>
<link href="https://fonts.googleapis.com/css2?family=Comfortaa:wght@400;500;700&display=swap" rel="stylesheet">
<style>
  :root {
    --paper: #ffffff;
    --cover-yellow: #f1d11a;
    --ink-red: #e84c3d;
    --ink-teal: #4e97a8;
    --steel-light: #aab5b8;
    --steel-dark: #6a6136;
  }
  * { margin: 0; padding: 0; box-sizing: border-box; }
  html, body {
    width: 1200px; height: 864px; overflow: hidden;
    background: var(--paper);
    font-family: "Comfortaa", sans-serif;
  }
  .spread { position: relative; width: 1200px; height: 864px; }
  .panel { position: absolute; background: var(--cover-yellow); }

  /* Back cover */
  .back-cover { left: 25px; top: 24px; width: 531px; height: 816px; }
  .synopsis {
    position: absolute; left: 29px; top: 26px; width: 474px;
    color: var(--ink-red);
    font-size: 18px; line-height: 20.3px; font-weight: 400;
    text-align: justify;
  }
  .synopsis p { text-indent: 17px; margin-bottom: 7px; }
  .publisher {
    position: absolute; right: 22px; top: 738px;
    color: var(--ink-teal);
    font-size: 24px; line-height: 29px; text-align: right;
  }

  /* Spine */
  .spine { left: 576px; top: 23px; width: 48px; height: 817px; }
  .spine-title {
    position: absolute; left: 50%; top: 50%;
    transform: translate(-50%, -50%) rotate(-90deg);
    white-space: nowrap;
    color: var(--ink-red);
    font-size: 25px; letter-spacing: 0.2px;
  }

  /* Front cover */
  .front-cover { left: 646px; top: 23px; width: 531px; height: 816px; }
  .title-main {
    position: absolute; left: 0; width: 100%; top: 22px;
    text-align: center; font-weight: 700; text-transform: uppercase;
    line-height: 1;
  }
  .title-main span {
    display: block;
    background: linear-gradient(180deg, var(--steel-light) 0%, var(--steel-dark) 50%, var(--steel-light) 100%);
    -webkit-background-clip: text; background-clip: text;
    color: transparent;
  }
  .title-main .line-one { font-size: 70px; letter-spacing: 1px; }
  .title-main .line-two { font-size: 104px; margin-top: 4px; }
  .subtitle {
    position: absolute; left: 0; width: 100%; top: 222px;
    text-align: center; text-transform: uppercase;
    font-size: 54px; line-height: 73.5px; font-weight: 500;
  }
  .subtitle .teal { color: var(--ink-teal); display: block; }
  .subtitle .red { color: var(--ink-red); display: block; }
  .authors {
    position: absolute; right: 29px; top: 548px;
    list-style: none; text-align: right;
    color: var(--ink-teal);
    font-size: 29px; line-height: 40.6px;
  }
</style>
</head>
<body>
<main class="spread">
  <section class="panel back-cover">
    <div class="synopsis">
      <p>The landscape of the publishing industry is changing. Gone are the days of coveted gatekeepers controlling content and dictating the messages being distributed. With the rise of technology, social media , self-publishing platforms, and independent bookstores, there are increased opportunities for people to share their ideas, messages, and stories with the world through books. The types of books that we’re publishing are also evolving – mini-books, audio books, journals, multi-author books, cook books, children’s books, comic books, coloring books, interactive books, tarot and oracle card decks are all expanding the podium for people to express ideas and influence the culture. More and more entrepreneurs are posturing themselves as thought leaders by leveraging this growing platform.</p>
      <p>But that doesn't mean it’s easy.</p>
      <p>Even with the expanding platforms and opportunities, only a fraction of people with publishing ambitions are able to achieve this coveted dream held by so many. It can be a daunting process for budding authors trying to maneuver through the writing, packaging, marketing, and publishing processes alone.</p>
    </div>
    <div class="publisher">Lantern Grove<br>Publishing</div>
  </section>

  <section class="panel spine">
    <div class="spine-title">Find Your Shelf! Veteran Editors Reveal Quiet Methods</div>
  </section>

  <section class="panel front-cover">
    <h1 class="title-main">
      <span class="line-one">Find Your</span>
      <span class="line-two">Shelf!</span>
    </h1>
    <h2 class="subtitle">
      <span class="teal">Veteran</span>
      <span class="red">Editors</span>
      <span class="teal">Reveal</span>
      <span class="red">Quiet Methods</span>
    </h2>
    <ul class="authors">
      <li>&gt;&gt;&gt; Autor 001 Halloran &gt;&gt;&gt;</li>
      <li>&gt;&gt;&gt; Autor 002 Pellister &gt;&gt;&gt;</li>
      <li>&gt;&gt;&gt; Autor 003 Dunmore &gt;&gt;&gt;</li>
      <li>&gt;&gt;&gt; Ivo 004 Renke &gt;&gt;&gt;</li>
      <li>&gt;&gt;&gt; Mara 005 Quill &gt;&gt;&gt;</li>
      <li>&gt;&gt;&gt; Tessa 006 Vale</li>
    </ul>
  </section>
</main>
</body>
</html>
```